KV HOLDINGS Business Cards

I need business cards for "KV Holdings group LLC" doublesided... logo on the back (also include logo on front)
logo attached to project... i have jpg up..
Company Info:
418 North Palmer Avenue, Suite 7B
Chicago, Illinois 60654
facsimile 312-555-0187 (list fax, address, website on all cards.)
www.kvholdingsgroup.example
Three different people on cards:
Darnell P. Okafor, CPA MST
Principal
ofc 312-555-0142
mobile 312-555-0169
darnellpokafor@kvholdingsgroup.example
Gregor T. Vanhoutte, CPA MST
Principal
gregortvanhoutte@kvholdingsgroup.example
mobile 708-555-0113
ofc 312-555-0142
Tobias M Quarrie
Principal
ofc 312-555-0142
no mobile
tobiasmquarrie@kvholdingsgroup.example
I have multiple projects listed.. see below:
Business cards for amber ledge partners llc
letterhead
envelopes
Business cards for KV Holdings LLC
letterhead
envelopes
Target Market(s)
rich people
Industry/Entity Type
Business

```html
<!DOCTYPE html>
<html lang="en">
<head>
<meta charset="utf-8">
<title>KV Holdings Group LLC – Business Cards</title>
<link rel="stylesheet" href="https://fonts.googleapis.com/css2?family=Saira:wght@400;500;600;700&display=swap">
<style>
  :root {
    --page: #e4e5e7;
    --royal-top: #0c63d6;
    --royal-bottom: #003e9c;
    --navy: #0d3a82;
    --ink: #1a1f2b;
    --brand-blue: #1f4c9e;
    --rule: #5a5f68;
    --faint: #b4c4da;
    --white: #ffffff;
  }
  * { box-sizing: border-box; margin: 0; padding: 0; }
  html, body { width: 1200px; height: 1012px; overflow: hidden; }
  body {
    background: var(--page);
    font-family: "Saira", "Arial Narrow", sans-serif;
    color: var(--ink);
    position: relative;
  }
  .card {
    position: absolute;
    left: 250px;
    width: 700px;
    height: 400px;
    overflow: hidden;
    box-shadow: 0 6px 18px rgba(0,0,0,.18);
  }
  /* Back side */
  .card--back {
    top: 71px;
    background: linear-gradient(180deg, var(--royal-top) 0%, var(--royal-bottom) 100%);
    display: flex;
    align-items: center;
    justify-content: center;
  }
  .brand { display: flex; align-items: center; gap: 12px; }
  .brand__mark { width: 18px; height: 18px; background: currentColor; }
  .brand__name { font-weight: 500; letter-spacing: .06em; text-transform: uppercase; }
  .card--back .brand { color: var(--white); }
  .card--back .brand__name { font-size: 30px; }
  .card--back .brand__mark { width: 24px; height: 24px; }

  /* Front side */
  .card--front { top: 541px; background: var(--white); }
  .card--front .brand {
    position: absolute; left: 40px; top: 34px; color: var(--brand-blue);
  }
  .card--front .brand__name { font-size: 19px; }
  .rule { position: absolute; height: 1.5px; background: var(--rule); }
  .rule--brand { left: 40px; top: 74px; width: 290px; }
  .rule--contact { left: 420px; top: 162px; width: 240px; }

  .office {
    position: absolute; right: 40px; top: 84px;
    text-align: right; color: var(--brand-blue);
    font-size: 12.5px; font-weight: 600; line-height: 1.3;
  }
  .section-title {
    position: absolute; right: 40px; top: 130px;
    font-size: 19px; font-weight: 700; color: var(--brand-blue);
  }

  .person { position: absolute; font-size: 11.5px; line-height: 1.32; }
  .person--gregor { left: 40px; top: 88px; }
  .person--darnell { left: 40px; top: 196px; }
  .person--tobias { left: 330px; top: 172px; }
  .person__row { display: flex; align-items: center; gap: 5px; white-space: nowrap; }
  .person__row--indent { padding-left: 16px; }
  .person__name { font-weight: 600; }
  .icon { width: 11px; height: 11px; flex: none; fill: var(--brand-blue); }

  .watermark-area {
    position: absolute; left: 330px; top: 236px; width: 330px; height: 120px;
    background: radial-gradient(ellipse at 45% 60%, var(--faint) 0%, rgba(180,196,218,.55) 55%, rgba(255,255,255,0) 78%);
  }
  .web-band { position: absolute; left: 0; bottom: 0; width: 700px; height: 80px; }
  .web-band__text {
    position: absolute; left: 150px; bottom: 16px;
    color: var(--white); font-size: 15px; font-weight: 600; letter-spacing: .02em;
  }
</style>
</head>
<body>

<section class="card card--back" aria-label="Card back">
  <div class="brand">
    <span class="brand__mark"></span>
    <span class="brand__name">KV Holdings Group LLC</span>
  </div>
</section>

<section class="card card--front" aria-label="Card front">
  <div class="brand">
    <span class="brand__mark"></span>
    <span class="brand__name">KV Holdings Group LLC</span>
  </div>
  <div class="rule rule--brand"></div>

  <address class="office">
    418 North Palmer Avenue, Suite 7B<br>
    Chicago, Illinois 60654<br>
    facsimile 312-555-0187
  </address>

  <h2 class="section-title">Contact Details</h2>
  <div class="rule rule--contact"></div>

  <svg width="0" height="0" style="position:absolute">
    <defs>
      <symbol id="i-person" viewBox="0 0 12 12"><circle cx="6" cy="3.5" r="2.7"/><path d="M1 12c0-3.2 2.2-5 5-5s5 1.8 5 5z"/></symbol>
      <symbol id="i-office" viewBox="0 0 12 12"><rect x="1" y="4" width="10" height="7.5" rx="1"/><rect x="2" y="1" width="8" height="2.5" rx="1"/></symbol>
      <symbol id="i-mobile" viewBox="0 0 12 12"><path d="M3 1l2 .2 1 2.6-1.3 1a6 6 0 0 0 2.5 2.5l1-1.3 2.6 1 .2 2-1.5 1.5C5 10.5 1.5 7 1.5 2.5z"/></symbol>
      <symbol id="i-mail" viewBox="0 0 12 12"><path d="M1 2.5h10v7H1z M1.5 3l4.5 3.5L10.5 3" fill="none" stroke="currentColor"/><rect x="1" y="2.5" width="10" height="7" rx=".6"/><path d="M1.5 3.2 6 6.6l4.5-3.4" fill="none" stroke="#fff" stroke-width="1"/></symbol>
    </defs>
  </svg>

  <div class="person person--gregor">
    <div class="person__row"><svg class="icon"><use href="#i-person"/></svg><span class="person__name">Gregor T. Vanhoutte, CPA MST</span></div>
    <div class="person__row person__row--indent">Principal</div>
    <div class="person__row"><svg class="icon"><use href="#i-office"/></svg>ofc 312-555-0142</div>
    <div class="person__row"><svg class="icon"><use href="#i-mobile"/></svg>mobile 708-555-0113</div>
    <div class="person__row"><svg class="icon"><use href="#i-mail"/></svg>gregortvanhoutte@kvholdingsgroup.example</div>
  </div>

  <div class="person person--darnell">
    <div class="person__row"><svg class="icon"><use href="#i-person"/></svg><span class="person__name">Darnell P. Okafor, CPA MST</span></div>
    <div class="person__row person__row--indent">Principal</div>
    <div class="person__row"><svg class="icon"><use href="#i-office"/></svg>ofc 312-555-0142</div>
    <div class="person__row"><svg class="icon"><use href="#i-mobile"/></svg>mobile 312-555-0169</div>
    <div class="person__row"><svg class="icon"><use href="#i-mail"/></svg>darnellpokafor@kvholdingsgroup.example</div>
  </div>

  <div class="person person--tobias">
    <div class="person__row"><svg class="icon"><use href="#i-person"/></svg><span class="person__name">Tobias M Quarrie</span></div>
    <div class="person__row person__row--indent">Principal</div>
    <div class="person__row"><svg class="icon"><use href="#i-office"/></svg>ofc 312-555-0142</div>
    <div class="person__row"><svg class="icon"><use href="#i-mail"/></svg>tobiasmquarrie@kvholdingsgroup.example</div>
  </div>

  <div class="watermark-area" role="img" aria-label="Large faint brand emblem decoration area"></div>

  <svg class="web-band" viewBox="0 0 700 80" preserveAspectRatio="none" aria-hidden="true">
    <path d="M130 30 Q180 12 700 14 L700 80 L130 80 Z" fill="#e9eef6"/>
    <path d="M110 80 Q130 34 200 34 L700 34 L700 72 L110 72 Z" fill="var(--navy)"/>
  </svg>
  <p class="web-band__text">Vsit our Website : www.kvholdingsgroup.example</p>
</section>

</body>
</html>
```